Business card design needed

would like the title calloway estate works to itself be a logo which would also be suitable to use on my van signwriting so needs to be bold and stand out (easily read from a distance)
Target Market(s)
real estate agents, property owners/investors,insurance assessors,
Industry/Entity Type
Business
Contact Information for Business Card
calloway estate works
for all your property maintenance and repair needs
-domestic and commercial -rental properties
-insurance repairs -project managment
fully insured/white card
experieced and reliable
ph. ned calloway 0418526093 email nedster4731@webhollow.net.au
on reverse side of card i would like a list of sevices available
plaster repairs
painting
welding reairs and fabrication
concreting
fencing
minor renovations
pressure cleaning
graffitti removal
rubbish removal
fire restorations
floods
and more no job too big or small
Logo Text
Logo styles of interest
Wordmark Logo

```html
<!DOCTYPE html>
<html lang="en">
<head>
<meta charset="utf-8">
<title>Calloway Estate Works – Business Card</title>
<link href="https://fonts.googleapis.com/css2?family=Source+Sans+3:ital,wght@0,400;0,600;0,700;1,700&family=Tinos:wght@700&family=Arimo:wght@700&display=swap" rel="stylesheet">
<style>
  :root {
    --stage: #8a8a8a;
    --front-brown: #4a2d0c;
    --panel-brown: #6b4215;
    --gold: #f5b50a;
    --orange: #e07a14;
    --white: #ffffff;
    --ink: #111111;
    --grey-text: #6e6e6e;
    --tag-text: #5a3a18;
  }
  html, body {
    margin: 0;
    padding: 0;
    width: 1200px;
    height: 1000px;
    overflow: hidden;
    background: var(--stage);
  }
  .canvas {
    position: relative;
    width: 1200px;
    height: 1000px;
  }
  .card {
    position: absolute;
    width: 706px;
    height: 436px;
    box-shadow: 0 10px 24px rgba(0,0,0,0.45);
    overflow: hidden;
  }

  /* Front */
  .card-front {
    left: 60px;
    top: 40px;
    background: var(--front-brown);
    font-family: "Source Sans 3", sans-serif;
    text-align: center;
  }
  .front-brand {
    margin: 130px 0 0;
    color: var(--gold);
    font-weight: 700;
    font-size: 46px;
    letter-spacing: 0.2px;
  }
  .front-services {
    margin: 26px 0 0;
    color: var(--white);
    font-size: 21px;
    line-height: 1.3;
  }
  .front-tagline {
    margin: 12px 0 0;
    color: var(--orange);
    font-style: italic;
    font-weight: 700;
    font-size: 20px;
    letter-spacing: 1px;
  }

  /* Back */
  .card-back {
    left: 430px;
    top: 520px;
    background: var(--white);
    display: flex;
  }
  .back-main {
    width: 496px;
    text-align: center;
    font-family: "Source Sans 3", sans-serif;
  }
  .back-brand {
    margin: 112px 0 0;
    color: var(--gold);
    font-weight: 700;
    font-size: 25px;
  }
  .back-services {
    margin: 6px 0 0;
    color: var(--tag-text);
    font-size: 12px;
    line-height: 1.2;
  }
  .contact-name {
    margin: 92px 0 0;
    font-family: "Tinos", serif;
    font-weight: 700;
    font-size: 30px;
    color: var(--ink);
  }
  .contact-details {
    margin: 62px 0 0;
    font-family: "Arimo", sans-serif;
    font-weight: 700;
    font-size: 21px;
    line-height: 1.3;
    color: var(--grey-text);
  }
  .services-panel {
    width: 210px;
    background: var(--panel-brown);
    color: var(--white);
    font-family: "Tinos", serif;
    font-weight: 700;
    font-size: 19px;
    text-align: center;
    line-height: 1.25;
    padding-top: 54px;
    box-sizing: border-box;
  }
  .services-title { margin: 0 0 24px; }
  .services-list { list-style: none; margin: 0; padding: 0; }
</style>
</head>
<body>
<div class="canvas">

  <section class="card card-front">
    <h1 class="front-brand">Calloway Estate Works</h1>
    <p class="front-services">Property Maintenance and Repair • Domestic and Commercial •<br>Rental Properties • Insurance Repairs • Project Managment</p>
    <p class="front-tagline">Fully Insured|White Card Experieced and Reliable</p>
  </section>

  <section class="card card-back">
    <div class="back-main">
      <h2 class="back-brand">Calloway Estate Works</h2>
      <p class="back-services">Property Maintenance and Repair • Domestic and Commercial •<br>Rental Properties • Insurance Repairs • Project Managment</p>
      <p class="contact-name">Ned Calloway</p>
      <p class="contact-details">Ph. 0418526093<br>email nedster4731@webhollow.net.au</p>
    </div>
    <aside class="services-panel">
      <p class="services-title">Sevices:</p>
      <ul class="services-list">
        <li>Plaster rRepairs</li>
        <li>Painting</li>
        <li>Welding Repairs</li>
        <li>and Fabrication</li>
        <li>Concreting</li>
        <li>Fencing</li>
        <li>Minor Renovations</li>
        <li>Pressure Cleaning</li>
        <li>Graffitti Removal</li>
        <li>Rubbish Removal</li>
        <li>Fire Restorations</li>
        <li>Floods and More</li>
      </ul>
    </aside>
  </section>

</div>
</body>
</html>
```